Kept Until Book Cover

I am looking for book front cover ideas. The book trim size will be 5.5 x 8.5 in so please make the mock up that size. The book Title is "Kept Until" and the Subtitle is "Insight for the Hard Calls Every Chief Faces". The audience for the book is leaders in high-growth companies. It consists of a series of letters and advice for specific problems the leader will encounter on their journey. The design needs to be attractive to both male and female readers. I am attaching a file with brand colors and some rough ideas that need to be refined. The examples lean toward a feminine vibe but I want the cover to be more universal. Please use the brand colors identified in the file.

```html
<!DOCTYPE html>
<html lang="en">
<head>
<meta charset="utf-8">
<title>Kept Until — Book Cover Spread</title>
<link href="https://fonts.googleapis.com/css2?family=Tenor+Sans&family=Abel&family=Arimo:ital@1&display=swap" rel="stylesheet">
<style>
  :root {
    --forest: #465a50;
    --clay: #a97a62;
    --cream: #f5f2ee;
    --page: #ffffff;
    --shadow: rgba(0, 0, 0, 0.38);
  }
  html, body {
    margin: 0;
    padding: 0;
    width: 1200px;
    height: 870px;
    overflow: hidden;
    background: var(--page);
  }
  .spread {
    position: relative;
    width: 1200px;
    height: 870px;
  }
  .back-cover, .front-cover {
    position: absolute;
    top: 140px;
    height: 606px;
    background: var(--cream);
    box-shadow: 3px 3px 4px var(--shadow);
    overflow: hidden;
  }
  .back-cover { left: 111px; width: 443px; }
  .front-cover { left: 643px; width: 445px; }

  .title {
    font-family: "Tenor Sans", sans-serif;
    text-transform: uppercase;
    line-height: 1;
    margin: 0;
    position: absolute;
    white-space: nowrap;
  }
  .title .line-one { color: var(--forest); display: block; }
  .title .line-two { color: var(--clay); display: block; }

  .back-cover .title {
    left: 0;
    right: 0;
    top: 46px;
    text-align: center;
    font-size: 52px;
    padding-left: 36px;
  }
  .back-cover .title .line-two { margin-top: -2px; }

  .blurb {
    position: absolute;
    left: 61px;
    top: 170px;
    width: 340px;
    font-family: "Abel", sans-serif;
    font-size: 9px;
    line-height: 11.7px;
    color: var(--forest);
  }
  .blurb p { margin: 0 0 11.7px 0; }

  .placeholder-block {
    position: absolute;
    background: var(--forest);
  }
  .placeholder-square { left: 95px; top: 445px; width: 93px; height: 94px; }
  .placeholder-wide { left: 245px; top: 459px; width: 116px; height: 55px; }

  .spine {
    position: absolute;
    left: 573px;
    top: 140px;
    width: 56px;
    height: 606px;
    background: var(--forest);
  }
  .spine-title {
    position: absolute;
    left: 50%;
    top: 186px;
    transform-origin: 0 0;
    transform: rotate(90deg) translateY(-50%);
    font-family: "Tenor Sans", sans-serif;
    font-size: 42px;
    line-height: 1;
    color: var(--cream);
    white-space: nowrap;
    text-transform: uppercase;
    letter-spacing: 1px;
  }

  .front-cover .title {
    left: 0;
    right: 0;
    top: 50px;
    text-align: center;
    font-size: 100px;
  }
  .front-cover .title .line-two { margin-top: -4px; }

  .base-band {
    position: absolute;
    left: 0;
    bottom: 0;
    width: 445px;
    height: 177px;
  }
  .tree-art {
    position: absolute;
    left: 66px;
    top: 236px;
    width: 336px;
    height: 283px;
    border-radius: 50% 50% 12% 12% / 60% 60% 10% 10%;
    background: radial-gradient(ellipse at 50% 55%, rgba(70, 90, 80, 0.85) 0%, rgba(70, 90, 80, 0.45) 55%, rgba(70, 90, 80, 0) 80%);
  }
  .subtitle {
    position: absolute;
    left: 0;
    right: 0;
    top: 549px;
    text-align: center;
    font-family: "Arimo", sans-serif;
    font-style: italic;
    font-size: 14.5px;
    color: var(--cream);
    margin: 0;
  }
</style>
</head>
<body>
<main class="spread">

  <section class="back-cover">
    <h2 class="title"><span class="line-one">Kept</span><span class="line-two">Until</span></h2>
    <div class="blurb">
      <p>Your inner world isn’t broken — it’s speaking. We spend much of our lives trying to understand what we feel — and even more time trying to change it.</p>
      <p>Anxiety, fear, heaviness, and confusion are often treated as problems to fix, rather than experiences asking to be understood.</p>
      <p>In What the Quiet Holds, Lena Marisol Haddad offers a gentler way of relating to our inner world. Drawing on years of working with people from diverse backgrounds, she explores how emotions arise, how beliefs shape our experience, and how meaning is created through perception rather than found outside us.</p>
      <p>This is not a book of quick fixes. It’s an invitation to slow down, to meet emotions with clarity and kindness, and to create meaning that feels honest and personal.</p>
      <p>For anyone who has ever felt overwhelmed by their inner world, this book offers understanding and a steadier way of being with what is.</p>
      <p>For deeper integration, a companion Practice &amp; Exercises Booklet is available separately and is highly recommended to get the most out of this book.</p>
    </div>
    <div class="placeholder-block placeholder-square"></div>
    <div class="placeholder-block placeholder-wide"></div>
  </section>

  <section class="spine">
    <span class="spine-title">Kept Until</span>
  </section>

  <section class="front-cover">
    <h1 class="title"><span class="line-one">Kept</span><span class="line-two">Until</span></h1>
    <svg class="base-band" viewBox="0 0 445 177" aria-hidden="true">
      <polygon points="0,0 223,104 445,0 445,177 0,177" fill="var(--forest)"/>
    </svg>
    <div class="tree-art" role="img" aria-label="Illustration of a broad leafy tree with spreading branches in forest green"></div>
    <p class="subtitle">Insight for the Hard Calls Every Chief Faces</p>
  </section>

</main>
</body>
</html>
```